The Duchess of Nestware is an online store specialising in all things for the home Bathroom, Kitchen,

I need a business card designed that is professional and elegant, yet not conservative. We will be wanting to brand the entire business and will have videos made where we will be interacting with the product, testing the products and basically creating an online interactive community for all those people interested in all things to do with the Home and the activities that take place in and around the home.

Target Market(s)

30-65yr old Men and Women who LOVE their Home and see it as their primary place of Happiness, their sanctuary!

Industry/Entity Type

Business

Contact Information for Business Card

www.duchessofnestware.example The Duchess Of Nestware-PO Box 58316, Marlow Flats, Auckland. NEW ZEALAND. info@duchessofnestware.example
Love your Home! Corinne Dale-Petrakou

Font styles to use
Decorative
Script

Colors
9bcb3b
33b8a4
85cae6
b7a5cd
eda3c7
e667a6
d2a4cc
fdf9cf
fee18a

Requirements
Must have
• Attractive colours. Must feel Elegant, yet simple. A font that is rounded without sharp edges. Organic feel to the card, something raw with texture.
Nice to have
• I like the logo deign that I gave in the photos, something feminine, but fun.
Should not have
• I dont like sharp edges, or linear design. I like organic, flowing, fractal type design. Something that looks beautiful in form when you look at it.

```html
<!DOCTYPE html>
<html lang="en">
<head>
<meta charset="utf-8">
<title>The Duchess of Nestware – Business Card</title>
<link rel="stylesheet" href="https://fonts.googleapis.com/css2?family=Playfair+Display:wght@700&family=Playball&family=Roboto:wght@400;500&display=swap">
<style>
  :root {
    --page-bg: #ffffff;
    --card-cream: #f9e8d6;
    --card-cream-light: #fbeedf;
    --swirl-tan: #ecc79a;
    --teal: #2eb3a0;
    --teal-deep: #1f9c8c;
    --gold: #b98a1c;
    --gold-light: #e7c55a;
    --gold-dark: #8f6a12;
    --shadow: rgba(60, 40, 20, 0.18);
  }
  * { box-sizing: border-box; margin: 0; padding: 0; }
  html, body { width: 1200px; height: 900px; overflow: hidden; background: var(--page-bg); }
  .canvas {
    position: relative; width: 1200px; height: 900px;
    display: flex; align-items: center; justify-content: center; gap: 40px;
  }
  .card {
    position: relative; width: 540px; height: 310px;
    border-radius: 22px; overflow: hidden;
    background: var(--card-cream);
    box-shadow: 0 14px 30px var(--shadow);
  }

  /* Front */
  .card-front__pattern {
    position: absolute; inset: 0;
    background:
      radial-gradient(ellipse at 30% 35%, var(--swirl-tan) 0%, transparent 55%),
      radial-gradient(ellipse at 75% 70%, var(--swirl-tan) 0%, transparent 55%),
      var(--card-cream);
    opacity: 0.75;
  }
  .card-front__brand {
    position: absolute; inset: 0;
    display: flex; align-items: center; justify-content: center;
    padding: 0 60px; text-align: center;
  }
  .brand-name {
    font-family: "Playfair Display", Georgia, serif;
    font-weight: 700; color: var(--teal);
    line-height: 1.1;
  }
  .card-front .brand-name { font-size: 46px; }

  /* Back */
  .card-back { background: var(--card-cream-light); }
  .card-back__frame {
    position: absolute; inset: 12px;
    border-radius: 16px;
    border: 5px solid var(--gold);
    box-shadow: inset 0 0 0 1px var(--gold-light), 0 0 0 1px var(--gold-light);
  }
  .card-back__brand { position: absolute; left: 34px; top: 50px; width: 300px; }
  .card-back .brand-name { font-size: 34px; }
  .holder-name {
    position: absolute; left: 34px; top: 152px;
    font-family: "Playball", cursive;
    font-size: 28px; color: var(--gold);
  }
  .contact { position: absolute; left: 34px; top: 196px; list-style: none; }
  .contact li {
    display: flex; align-items: center; gap: 8px;
    font-family: "Roboto", Arial, sans-serif;
    font-size: 13px; line-height: 16px; color: var(--teal);
  }
  .contact .contact__indent { padding-left: 22px; }
  .contact .contact__strong { font-weight: 500; color: var(--teal-deep); }
  .contact svg { width: 14px; height: 14px; flex: none; }
  .social { position: absolute; right: 36px; top: 232px; display: flex; gap: 6px; }
  .social span {
    width: 16px; height: 16px; border-radius: 50%;
    background: radial-gradient(circle at 35% 35%, var(--gold-light), var(--gold-dark));
  }
</style>
</head>
<body>
<main class="canvas">
  <section class="card card-front" aria-label="Business card front">
    <div class="card-front__pattern" role="img" aria-label="Flowing tan swirl and dot pattern across the card"></div>
    <div class="card-front__brand">
      <p class="brand-name">The Duchess of Nestware</p>
    </div>
  </section>

  <section class="card card-back" aria-label="Business card back">
    <div class="card-back__frame"></div>
    <div class="card-back__brand">
      <p class="brand-name">The Duchess of Nestware</p>
    </div>
    <p class="holder-name">Corinne Dale-Petrakou</p>
    <ul class="contact">
      <li class="contact__indent">The Duchess Of Nestware</li>
      <li>
        <svg viewBox="0 0 16 16" aria-hidden="true"><path d="M8 1.5a4.5 4.5 0 0 0-4.5 4.5c0 3.3 4.5 8.5 4.5 8.5s4.5-5.2 4.5-8.5A4.5 4.5 0 0 0 8 1.5z" fill="none" stroke="#b98a1c" stroke-width="1.6"/><circle cx="8" cy="6" r="1.6" fill="#b98a1c"/></svg>
        PO Box 58316, Marlow Flats
      </li>
      <li class="contact__indent contact__strong">Auckland. NEW ZEALAND.</li>
      <li>
        <svg viewBox="0 0 16 16" aria-hidden="true"><g fill="none" stroke="#b98a1c" stroke-width="1.3"><circle cx="8" cy="8" r="6.2"/><ellipse cx="8" cy="8" rx="2.8" ry="6.2"/><path d="M1.8 8h12.4M2.8 5h10.4M2.8 11h10.4"/></g></svg>
        www.duchessofnestware.example
      </li>
      <li>
        <svg viewBox="0 0 16 16" aria-hidden="true"><rect x="1.5" y="3.5" width="13" height="9" rx="1" fill="#b98a1c"/><path d="M2 4l6 5 6-5" fill="none" stroke="#fbeedf" stroke-width="1.3"/></svg>
        info@duchessofnestware.example
      </li>
    </ul>
    <div class="social" aria-label="Social links">
      <span></span><span></span><span></span>
    </div>
  </section>
</main>
</body>
</html>
```